Bayline Pet Rehoming GALA

Hi ALL!
We need an 8.5 X 11 inch, one page flyer to include all the below copy plus 8 sponsoring logos at the very bottom.
Thank YOU!

Corvel Heights Pet GALA
(Fun for Animals In Rescue!)

Sunday, August 12, 2018
1 to 4:30 p.m.

Animal Education & Adoption Event
featuring:

BK Pet Shelter & Services Rabbits & Mice

Hilltop Browsing Sheep

Thankful Hounds Haven

Featherwell Finches & Larks

Comet Pup Haven

Marla’s Feline Haven

Marvel Pup Haven

Special Guest from 1-3 p.m.
BeeBop - SF's 1st Therapy Pig!
Instagram: @BEEBOP_BKHOG
Facebook: @BEEBOP THE HOG

Activities for Kids
Dog & Cat Toy Making with Greta Vossel Canine Coaching
Animal Mask Making with Tiny Crafters
Face-in-a-Hole Photo Fun with Hugo Marsh Canine Coaching

BK PSS FREE Giveaway!
First 75 attending families receive a FREE PSS Doggie Bag containing a dog water bottle, food, shampoo, toy, treats and blinking dog collar light.

Animal Tails

1 pm Wendell’s Nook Storytime

1:30 p.m. BeeBop the Therapy Pig

1:45 pm “Tuft the Saved Hog”
Read by Author Marnie Oakhurst

2 p.m. Wendell’s Nook Singalong

2:30 p.m. Featherwell Finch Haven

2:45 p.m. Quire Pages Storytime

3 pm Browsing Sheep Refuge

3:15 p.m. The Burrow Den Puppet Show

3:45 pm BK PSS Officer Tamsin

4 p.m. Wendell’s Nook Storytime

Font styles to use
Serif

Colors

Designer to choose colors to be used in the design.

Requirements
Must have
• pig, goat, 2 dogs, kitten, dove, bunny

```html
<!DOCTYPE html>
<html lang="en">
<head>
<meta charset="utf-8">
<title>Corvel Heights Pet GALA</title>
<link href="https://fonts.googleapis.com/css2?family=Montserrat:wght@400;500;600;700&family=Oswald:wght@400&display=swap" rel="stylesheet">
<style>
  :root {
    --blue: #1b5c9e;
    --green: #6aa321;
    --yellow: #f4e52a;
    --red: #e02222;
    --ink: #2b2b2b;
    --row-shade: #d9d9d9;
    --rule: #9a9a9a;
    --page-bg: #e9e9e9;
  }
  html, body { margin: 0; padding: 0; width: 1200px; height: 1200px; overflow: hidden; background: var(--page-bg); }
  .flyer {
    position: absolute; left: 152px; top: 20px;
    width: 918px; height: 1190px; background: #fff;
    transform: scale(0.975); transform-origin: top left;
    font-family: "Montserrat", sans-serif; color: var(--ink);
    box-shadow: 0 2px 10px rgba(0,0,0,.15);
  }
  .abs { position: absolute; }
  .hero {
    left: 0; top: 0; width: 918px; height: 455px;
    background: linear-gradient(#bfe3f3 0%, #e6f4fa 55%, #ffffff 75%, #ffffff 100%);
  }
  .title { left: 0; width: 918px; top: 462px; text-align: center; color: var(--blue); font-weight: 700; font-size: 51px; letter-spacing: 1px; margin: 0; }
  .subtitle { left: 0; width: 918px; top: 522px; text-align: center; font-size: 33px; margin: 0; font-weight: 400; }
  .date { left: 0; width: 918px; top: 568px; text-align: center; font-size: 27px; font-weight: 700; color: var(--green); margin: 0; }
  .date .time { color: var(--blue); }

  .featuring { left: 42px; top: 627px; width: 416px; height: 175px; border: 1px solid #bbb; border-radius: 3px; overflow: hidden; }
  .featuring h2 { margin: 0; height: 31px; line-height: 31px; background: var(--blue); color: #fff; font-size: 14.5px; letter-spacing: -0.3px; font-weight: 700; padding-left: 9px; white-space: nowrap; }
  .featuring ul { position: absolute; margin: 0; padding: 0; list-style: none; font-size: 14px; line-height: 18px; }
  .featuring li { position: absolute; padding-left: 15px; white-space: nowrap; }
  .featuring li::before { content: ""; position: absolute; left: 0; top: 6px; width: 6px; height: 6px; border-radius: 50%; border: 1.5px solid var(--blue); background: var(--blue); box-shadow: inset 0 0 0 1px #fff; }
  .col-a { left: 11px; top: 38px; }
  .col-b { left: 233px; top: 38px; }

  .pill { background: var(--blue); color: #fff; font-size: 14.5px; font-weight: 500; border-radius: 0 8px 8px 0; height: 22px; line-height: 22px; padding: 0 9px 0 7px; }
  .activities-pill { left: 43px; top: 820px; }
  .activities { left: 43px; top: 846px; width: 425px; font-size: 13.5px; line-height: 18px; margin: 0; white-space: nowrap; }
  .giveaway-head { left: 43px; top: 915px; font-size: 22px; font-weight: 500; color: var(--blue); margin: 0; }
  .free { color: var(--red); }
  .giveaway-text { left: 43px; top: 941px; width: 425px; font-size: 14.5px; line-height: 18px; font-weight: 600; margin: 0; }
  .sponsor-pill { left: 43px; top: 1014px; }
  .logo-slot { width: 93px; height: 48px; border: 1px solid #bdbdbd; }

  .schedule { left: 501px; top: 627px; width: 371px; border-collapse: collapse; font-size: 14.5px; border: 1px solid var(--rule); }
  .schedule th { background: var(--green); color: #fff; height: 33px; font-size: 19px; font-weight: 700; }
  .schedule td { height: 36px; padding: 0; vertical-align: middle; line-height: 18px; white-space: nowrap; }
  .schedule td.when { width: 112px; padding-left: 22px; box-sizing: border-box; border-right: 1px solid var(--rule); font-weight: 500; }
  .schedule td.what { padding-left: 13px; }
  .schedule tr.shade td { background: var(--row-shade); }
  .schedule tr.tall td { height: 48px; }

  .guest { left: 501px; top: 1044px; width: 372px; height: 63px; background: var(--green); border-radius: 4px; color: #fff; text-align: center; font-size: 20px; font-weight: 700; line-height: 25px; padding-top: 7px; box-sizing: border-box; box-shadow: 0 1px 2px rgba(0,0,0,.3); }
  .guest .hours { color: var(--yellow); }
  .follow-line { left: 500px; top: 1126px; width: 372px; display: flex; align-items: center; justify-content: space-between; white-space: nowrap; }
  .follow { font-family: "Oswald", sans-serif; color: var(--red); font-size: 17px; }
  .social { font-size: 12px; font-weight: 500; display: flex; align-items: center; gap: 5px; }
  .social .mark { width: 15px; height: 15px; background: #555; display: inline-block; }
  .footer-band { left: 0; top: 1173px; width: 918px; height: 17px; background: var(--blue); }
</style>
</head>
<body>
<main class="flyer">
  <div class="abs hero" role="img" aria-label="Photo of rescue animals against a sky: a goat, a bunny, a kitten, a flying dove, two shepherd dogs and a piglet"></div>

  <h1 class="abs title">CORVEL HEIGHTS PET GALA</h1>
  <p class="abs subtitle">(Fun for Animals In Rescue!)</p>
  <p class="abs date">Sunday, August 12, 2018 <span class="time">1 to 4:30 p.m.</span></p>

  <section class="abs featuring">
    <h2>Animal Education &amp; Adoption Event featuring:</h2>
    <ul class="col-a">
      <li style="top:0">BK Pet Shelter &amp; Services<br>Rabbits &amp; Mice</li>
      <li style="top:45px">Hilltop Browsing Sheep</li>
      <li style="top:72px">Thankful Hounds Haven</li>
      <li style="top:99px">Featherwell Finches<br>&amp; Larks</li>
    </ul>
    <ul class="col-b">
      <li style="top:0">Comet Pup Haven</li>
      <li style="top:36px">Marla’s Feline Haven</li>
      <li style="top:72px">Marvel Pup Haven</li>
    </ul>
  </section>

  <div class="abs pill activities-pill">Activities for Kids</div>
  <p class="abs activities">Dog &amp; Cat Toy Making with Greta Vossel Canine Coaching<br>Animal Mask Making with Tiny Crafters<br>Face-in-a-Hole Photo Fun with Hugo Marsh Canine Coaching</p>

  <h2 class="abs giveaway-head">BK PSS <span class="free">FREE</span> Giveaway!</h2>
  <p class="abs giveaway-text">First 75 attending families receive a <span class="free">FREE</span> PSS Doggie Bag containing a dog water bottle, food, shampoo, toy, treats and blinking dog collar light.</p>

  <div class="abs pill sponsor-pill">8 sponsoring logos</div>
  <div class="abs logo-slot" style="left:43px;top:1045px"></div>
  <div class="abs logo-slot" style="left:151px;top:1045px"></div>
  <div class="abs logo-slot" style="left:259px;top:1045px"></div>
  <div class="abs logo-slot" style="left:367px;top:1045px"></div>
  <div class="abs logo-slot" style="left:43px;top:1105px"></div>
  <div class="abs logo-slot" style="left:151px;top:1105px"></div>
  <div class="abs logo-slot" style="left:259px;top:1105px"></div>
  <div class="abs logo-slot" style="left:367px;top:1105px"></div>

  <table class="abs schedule">
    <thead><tr><th colspan="2">Animal Tails</th></tr></thead>
    <tbody>
      <tr class="shade"><td class="when">1 p.m.</td><td class="what">Wendell’s Nook Storytime</td></tr>
      <tr><td class="when">1:30 p.m.</td><td class="what">BeeBop the Therapy Pig</td></tr>
      <tr class="shade tall"><td class="when">1:45 p.m.</td><td class="what">“Tuft the Saved Hog”<br>Read by Author Marnie Oakhurst</td></tr>
      <tr><td class="when">2:00 p.m.</td><td class="what">Wendell’s Nook Singalong</td></tr>
      <tr class="shade"><td class="when">2:30 p.m.</td><td class="what">Featherwell Finch Haven</td></tr>
      <tr><td class="when">2:45 p.m.</td><td class="what">Quire Pages Storytime</td></tr>
      <tr class="shade"><td class="when">3:00 p.m.</td><td class="what">Browsing Sheep Refuge</td></tr>
      <tr><td class="when">3:15 p.m.</td><td class="what">The Burrow Den Puppet Show</td></tr>
      <tr class="shade"><td class="when">3:45 p.m.</td><td class="what">BK PSS Officer Tamsin</td></tr>
      <tr><td class="when">4 p.m.</td><td class="what">Wendell’s Nook Storytime</td></tr>
    </tbody>
  </table>

  <div class="abs guest">Special Guest from <span class="hours">1-3 p.m.</span><br>BeeBop - SF's 1st Therapy Pig!</div>

  <div class="abs follow-line">
    <span class="follow">FOLLOW US:</span>
    <span class="social"><span class="mark"></span>@BEEBOP_BKHOG</span>
    <span class="social"><span class="mark"></span>@BEEBOP THE HOG</span>
  </div>

  <div class="abs footer-band"></div>
</main>
</body>
</html>
```